Criação de Logotipo + Papelaria Profissional + Manual para Arquitetura
A empresa queria:
" Trata-se de uma empresa do ramo de arquitetura e urbanismo, formada por um casal de jovens arquitetos. Os serviços podem ser prestados presencialmente através do contato direto com o cliente ou ainda por meio da internet, onde a abordagem com o cliente se dá através das redes sociais. A empresa pretende ampliar sua atuação na internet através do marketing digital e para isto necessita transmitir com clareza valores como: credibilidade, contemporaneidade, versatilidade e objetividade. "

```html
<!DOCTYPE html>
<html lang="pt-BR">
<head>
<meta charset="utf-8">
<title>Vertiza — Cartão de visita</title>
<link rel="stylesheet" href="https://fonts.googleapis.com/css2?family=Montserrat:wght@400;500;600&family=Quicksand:wght@500;600&display=swap">
<style>
  :root {
    --page: #e9e9ea;
    --graphite: #3b3d40;
    --graphite-deep: #2f3134;
    --orange: #ee7a1a;
    --white: #ffffff;
    --ink: #3a3a3a;
    --soft-gray: #d9dadb;
  }
  * { box-sizing: border-box; margin: 0; padding: 0; }
  html, body { width: 1200px; height: 1200px; overflow: hidden; }
  body {
    background: var(--page);
    font-family: "Montserrat", sans-serif;
    position: relative;
  }
  .card {
    position: absolute;
    left: 258px;
    width: 684px;
    height: 420px;
    border-radius: 28px;
    overflow: hidden;
  }
  .card-front { top: 150px; background: var(--graphite); }
  .card-back { top: 630px; background: var(--white); }
  .card-band { position: absolute; left: 0; bottom: 0; width: 100%; height: 90px; }

  .brand { display: flex; flex-direction: column; align-items: center; }
  .brand-mark { width: 70px; height: 70px; background: var(--orange); margin-bottom: 22px; }
  .brand-name {
    font-family: "Quicksand", sans-serif;
    font-weight: 600;
    font-size: 62px;
    letter-spacing: 4px;
    line-height: 1;
  }
  .brand-tagline {
    font-size: 15px;
    letter-spacing: 3px;
    color: var(--orange);
    margin-top: 6px;
  }
  .card-front .brand { position: absolute; top: 56px; left: 0; width: 100%; }
  .card-front .brand-name { color: var(--white); }
  .front-url {
    position: absolute; top: 300px; width: 100%;
    text-align: center; color: var(--white);
    font-size: 21px; letter-spacing: 2px;
  }

  .card-back .brand { position: absolute; left: 30px; top: 128px; width: 280px; }
  .card-back .brand-name { color: var(--graphite); font-size: 56px; }
  .card-back .brand-tagline { font-size: 14px; }

  .contact { position: absolute; left: 352px; top: 50px; width: 320px; color: var(--ink); }
  .contact-name { font-size: 20px; font-weight: 500; }
  .contact-role { font-size: 16px; margin-top: 4px; margin-bottom: 18px; }
  .contact-list { list-style: none; }
  .contact-item { display: flex; align-items: center; gap: 10px; font-size: 16px; margin-bottom: 12px; line-height: 1.25; }
  .contact-item svg { flex: none; width: 28px; height: 28px; }
</style>
</head>
<body>

<section class="card card-front">
  <div class="brand">
    <div class="brand-mark"></div>
    <div class="brand-name">VERTIZA</div>
    <div class="brand-tagline">ARQUITETURA E INTERIORES</div>
  </div>
  <p class="front-url">www.vertiza.com.br</p>
  <svg class="card-band" viewBox="0 0 684 90" preserveAspectRatio="none">
    <path d="M0 62 H640 Q670 62 684 40 V90 H0 Z" fill="var(--orange)"/>
    <path d="M0 58 H640 Q665 58 684 30 V40 Q670 62 640 62 H0 Z" fill="var(--graphite-deep)"/>
  </svg>
</section>

<section class="card card-back">
  <div class="brand">
    <div class="brand-mark"></div>
    <div class="brand-name">VERTIZA</div>
    <div class="brand-tagline">ARQUITETURA E INTERIORES</div>
  </div>

  <div class="contact">
    <p class="contact-name">Nome e Sobrenome</p>
    <p class="contact-role">ARQUITETO - CAU 12345</p>
    <ul class="contact-list">
      <li class="contact-item">
        <svg viewBox="0 0 28 28"><circle cx="14" cy="14" r="14" fill="var(--orange)"/><path d="M10 8 l3 3 -2 2 q1.5 3 4 4 l2 -2 3 3 -2 2 q-6 0 -10 -10 z" fill="var(--white)"/></svg>
        (11) 4002-3150
      </li>
      <li class="contact-item">
        <svg viewBox="0 0 28 28"><circle cx="14" cy="14" r="14" fill="var(--orange)"/><rect x="10" y="7" width="8" height="14" rx="1.5" fill="none" stroke="var(--white)" stroke-width="1.8"/><circle cx="14" cy="18" r="1" fill="var(--white)"/></svg>
        (11) 4002-3150
      </li>
      <li class="contact-item">
        <svg viewBox="0 0 28 28"><circle cx="14" cy="14" r="14" fill="var(--orange)"/><rect x="8" y="9.5" width="12" height="9" fill="none" stroke="var(--white)" stroke-width="1.6"/><path d="M8 9.5 l6 5 6 -5" fill="none" stroke="var(--white)" stroke-width="1.6"/></svg>
        contato@vertiza.com.br
      </li>
      <li class="contact-item">
        <svg viewBox="0 0 28 28"><circle cx="14" cy="14" r="14" fill="var(--orange)"/></svg>
        /vertizaarquitetura
      </li>
      <li class="contact-item">
        <svg viewBox="0 0 28 28"><circle cx="14" cy="14" r="14" fill="var(--orange)"/><path d="M14 21 q-5 -5.5 -5 -9 a5 5 0 0 1 10 0 q0 3.5 -5 9 z" fill="var(--white)"/><circle cx="14" cy="12" r="1.8" fill="var(--orange)"/></svg>
        <span>Av. Horizonte Claro, 1300 | Centro<br>CEP: 04120-300 | São Paulo/SP</span>
      </li>
    </ul>
  </div>

  <svg class="card-band" viewBox="0 0 684 90" preserveAspectRatio="none">
    <path d="M0 70 H200 V90 H0 Z" fill="var(--soft-gray)"/>
    <path d="M150 90 Q190 62 240 62 H684 V90 Z" fill="var(--orange)"/>
  </svg>
</section>

</body>
</html>
```